Healthy Supplement featuring Moringa products

Need 3 business card options for our reps to order from Cardloom. Our reps will be ordering from Cardloom once we upload them. Attached is our current designs to show what info needs to be on the cards. Our website is www.tkvitality.com
The business cards will be a template for our reps to order from. Most of our reps are Asian & Hispanic. Please look at our website so you can see who we are to get the look and feel what we need.
Target Market(s)
Adults 30 on up. Health oriented people.
Industry/Entity Type
Health And Wellness
Contact Information for Business Card
Name
Title
Phone
Logo
www.tkvitality.com/my/username
Font styles to use
Requirements
Must have
- Please match our website look and colors. A moringa leaf is nice, but am open to something different.
Nice to have
- Healthy looking and warm, not super cold or too modern.
Should not have
- No harsh colors please.

```html
<!DOCTYPE html>
<html lang="en">
<head>
<meta charset="utf-8">
<title>TK Vitality Business Card – Option 02</title>
<link rel="stylesheet" href="https://fonts.googleapis.com/css2?family=Open+Sans:wght@400;600&display=swap">
<style>
  :root {
    --page-bg: #ffffff;
    --card-white: #ffffff;
    --card-border: #d4d4d4;
    --leaf-green: #6aaa3f;
    --lime: #abcf38;
    --lime-deep: #8fbc3a;
    --ink: #3b3b3b;
    --white: #ffffff;
    --shadow: rgba(0, 0, 0, 0.28);
  }
  * { box-sizing: border-box; margin: 0; padding: 0; }
  html, body {
    width: 1200px; height: 1200px; overflow: hidden;
    background: var(--page-bg);
    font-family: "Open Sans", Arial, sans-serif;
    color: var(--ink);
  }
  .sheet { position: relative; width: 1200px; height: 1200px; }
  .card {
    position: absolute; left: 296px; width: 618px; height: 370px;
    box-shadow: 18px 18px 22px -6px var(--shadow);
    overflow: hidden;
  }
  .card--front { top: 200px; background: var(--card-white); border: 1px solid var(--card-border); }
  .card--back { top: 639px; background: var(--lime); }

  .brand { position: absolute; display: flex; align-items: center; gap: 10px; font-weight: 600; letter-spacing: 1px; }
  .brand__dot { display: block; border-radius: 50%; }
  .card--front .brand { left: 72px; top: 118px; color: var(--leaf-green); font-size: 30px; }
  .card--front .brand__dot { width: 30px; height: 30px; background: var(--leaf-green); }

  .rep { position: absolute; right: 388px; top: 244px; text-align: right; }
  .rep__name { font-size: 19px; font-weight: 600; line-height: 26px; }
  .rep__title { font-size: 19px; font-weight: 400; line-height: 24px; }

  .divider {
    position: absolute; left: 264px; top: 229px; height: 102px;
    border-left: 2px dashed var(--leaf-green);
  }
  .contact { position: absolute; left: 286px; top: 245px; list-style: none; font-size: 16.5px; line-height: 27px; }

  .card--back .brand { left: 123px; top: 126px; color: var(--white); font-size: 18px; }
  .card--back .brand__dot { width: 18px; height: 18px; background: var(--white); }
  .back-url { position: absolute; left: 126px; top: 185px; color: var(--white); font-size: 16.5px; }
  .foliage {
    position: absolute; left: 251px; top: 10px; width: 367px; height: 360px;
    background: radial-gradient(ellipse at 65% 55%, rgba(106,170,63,0.55), rgba(143,188,58,0.25) 60%, rgba(171,207,56,0) 80%);
  }
  .option-label { position: absolute; right: 57px; top: 1151px; font-size: 17.5px; color: var(--ink); }
</style>
</head>
<body>
<main class="sheet">
  <section class="card card--front" aria-label="Business card front">
    <div class="brand"><span class="brand__dot"></span><span>TK VITALITY</span></div>
    <div class="rep">
      <p class="rep__name">Name</p>
      <p class="rep__title">Title</p>
    </div>
    <span class="divider"></span>
    <ul class="contact">
      <li>(000) 000-000</li>
      <li>email@address.com</li>
      <li>www.tkvitality.com/my/username</li>
    </ul>
  </section>

  <section class="card card--back" aria-label="Business card back">
    <div class="foliage" role="img" aria-label="Hand-drawn green moringa leaf branches"></div>
    <div class="brand"><span class="brand__dot"></span><span>TK VITALITY</span></div>
    <p class="back-url">www.tkvitality.com</p>
  </section>

  <p class="option-label">Option 02</p>
</main>
</body>
</html>
```